Double-Sided Tri-fold Brochure Needed for PTSD Service Dog Organization that serves US Veterans and

Our current brochure is in desperate need of a face lift. We want something fresh and are open to all ideas. We need our new logo added, we want to change some text around and add more information, and we want to update it with current photos. Text, I imagine, can be changed after winning design is selected. We use our brochure for fundraising, so we'd love to have it easy to read, yet able to make an emotional impact. We need to keep the donation mail-in form already on the old brochure. We are open to artist interpretations, however, for color scheme reference our website is: www.BlueMeadowCanineAllies.com

Target Market(s)

Veterans, First-Responders, Dog Lovers, Donors

Industry/Entity Type

It Service

Requirements
Must have
• Able to elicit an emotional response. We use our brochures for fundraising and information.
Should not have
• anything "cute"

```html
<!DOCTYPE html>
<html lang="en">
<head>
<meta charset="utf-8">
<title>Blue Meadow Canine Allies – Tri-fold Brochure</title>
<link href="https://fonts.googleapis.com/css2?family=Oswald:wght@500;600&family=Raleway:wght@400;500;600;700&display=swap" rel="stylesheet">
<style>
:root{
  --green:#3f6b36;
  --green-dark:#2f5428;
  --red:#b0261c;
  --ink:#4d4d4d;
  --paper:#ffffff;
  --paper-grey:#f2f2f2;
  --line:#9a9a9a;
  --stage:#e8e5e0;
}
*{box-sizing:border-box;margin:0;padding:0}
html,body{width:960px;height:1200px;overflow:hidden;background:var(--stage)}
body{position:relative;font-family:"Raleway",sans-serif;color:var(--ink)}
.sheet{position:absolute;left:133px;width:693px;height:490px;background:var(--paper);overflow:hidden;box-shadow:0 2px 8px rgba(0,0,0,.15)}
.sheet--outside{top:79px}
.sheet--inside{top:631px}
.abs{position:absolute}

/* outside: donation form */
.form-area{left:0;top:0;width:460px;height:490px;background:var(--paper-grey)}
.form-backdrop{left:150px;top:0;width:310px;height:490px;background:radial-gradient(ellipse at 55% 45%,#dcdcdc 0%,#ebebeb 45%,rgba(242,242,242,0) 75%)}
.form-icon{left:14px;top:22px;width:30px;height:30px}
.form-title{left:52px;top:17px;font-size:12.5px;font-weight:700;line-height:13px;color:var(--green)}
.form-title .accent{color:var(--red)}
.form-card{left:8px;top:65px;width:214px;height:348px;background:var(--paper);border-radius:8px;padding:8px 11px 0 12px}
.field{display:flex;align-items:flex-end;height:18.4px;font-size:7.4px;white-space:nowrap}
.field .rule{flex:1;border-bottom:.8px solid var(--line);margin-left:1px;height:8px}
.field .gap{width:10px}
.field .box{display:inline-block;width:6px;height:6px;border:.8px solid var(--ink);margin:0 5px 0 14px;vertical-align:-1px}
.form-note{left:12px;top:422px;width:200px;text-align:center;font-size:7.2px;line-height:10.8px}
.form-note b{font-weight:700}
.mini-brand{left:262px;top:412px;display:flex;align-items:center;gap:5px;font-family:"Oswald",sans-serif;font-weight:600;font-size:9px;line-height:10px;color:var(--green)}
.mini-brand .mark{width:14px;height:14px;background:var(--green)}

/* outside: cover */
.cover-brand{left:568px;top:30px;width:96px;font-family:"Oswald",sans-serif;font-weight:600;font-size:17px;line-height:18px;color:var(--green)}
.cover-brand .mark{display:block;width:16px;height:16px;background:var(--green);margin-bottom:6px}
.cover-shape{left:460px;top:240px}
.cover-photo{left:445px;top:169px;width:160px;height:160px;border-radius:50%;background:radial-gradient(circle at 55% 45%,#bdbdbd,#7a7a7a 60%,#4e4e4e);border:4px solid var(--paper);box-shadow:0 0 0 4px var(--green)}
.cover-title{left:482px;top:368px;font-family:"Oswald",sans-serif;font-weight:600;font-size:23px;line-height:26.5px;color:#fff;letter-spacing:-.2px}
.cover-url{left:672px;top:486px;transform:rotate(-90deg);transform-origin:0 0;font-size:7.6px;font-weight:600;color:var(--green);white-space:nowrap}

/* inside panels */
.panel-green{left:231px;top:0;width:230px;height:490px;background:var(--green)}
.body-text{font-size:7.9px;line-height:9.6px}
.intro{left:11px;top:21px;width:124px}
.section-title{font-size:13px;font-weight:700;color:var(--green)}
.mission-title{left:11px;top:233px}
.mission-text{left:11px;top:249px;width:212px}
.reality-title{left:11px;top:336px}
.reality-list{left:11px;top:357px;width:200px;list-style:none;font-size:7.9px;line-height:13px}
.reality-list li{margin-bottom:8px;padding-left:7px;text-indent:-7px}
.photo{position:absolute;border-radius:50%;border:3px solid #fff;box-shadow:0 0 0 3px var(--green)}
.photo--dark{background:radial-gradient(circle at 50% 45%,#8a7a66,#4a4038 70%)}
.photo--light{background:radial-gradient(circle at 50% 45%,#d9d2c4,#8c8376 70%)}
.hope-title{left:289px;top:20px;font-size:13.5px;font-weight:700;color:#fff}
.hope-list{left:289px;top:45px;width:156px;list-style:none;color:#fff;font-size:7.7px;line-height:9.6px}
.hope-list li{position:relative;padding-left:9px;margin-bottom:9.5px}
.hope-list li::before{content:"";position:absolute;left:0;top:2.5px;width:4px;height:4px;border-radius:50%;background:#fff}
.banner{left:468px;top:13px;width:214px;height:100px;background:linear-gradient(90deg,#3b3a33 0%,#5b5546 45%,#2b2a25 100%)}
.banner-line1{left:491px;top:70px;font-size:13px;font-weight:600;color:#fff}
.banner-line2{left:566px;top:88px;font-size:9px;color:#fff;border-bottom:.8px solid #fff;padding-bottom:1px}
.help-title{left:471px;top:127px}
.help-text{left:471px;top:149px;width:211px;font-size:7.8px;line-height:9.4px;text-align:justify}
.help-text b{font-weight:700;color:#333}
.consider{left:471px;top:220px;font-size:8.2px;font-weight:600;color:#333}
.give-list{left:471px;top:235px;list-style:none;font-size:7.8px;line-height:14.6px}
.give-jar{left:567px;top:247px;width:100px;height:100px}
.sponsor{left:491px;top:375px;width:190px;font-size:8px;line-height:12px;font-weight:700;color:var(--red)}
.contact{left:493px;top:432px;font-size:8px;line-height:15.5px;color:#333}
.contact .phone{font-weight:700;font-size:9.5px}
</style>
</head>
<body>

<!-- Outside sheet -->
<section class="sheet sheet--outside">
  <div class="abs form-area"></div>
  <div class="abs form-backdrop" role="img" aria-label="Faint photo of a uniformed soldier behind the form"></div>

  <svg class="abs form-icon" viewBox="0 0 30 30" aria-hidden="true">
    <rect x="3" y="13" width="24" height="15" fill="#3f6b36"/>
    <rect x="9" y="13" width="12" height="2" fill="#fff"/>
    <circle cx="15" cy="7" r="5" fill="#3f6b36"/>
  </svg>
  <h2 class="abs form-title">Every Contribution Helps<br><span class="accent">Us Make a Difference in<br>a Veteran’s Life!</span></h2>

  <div class="abs form-card">
    <div class="field">Name<span class="rule"></span></div>
    <div class="field">Phone<span class="rule"></span></div>
    <div class="field">Address<span class="rule"></span></div>
    <div class="field"><span class="rule"></span></div>
    <div class="field"><span class="rule"></span></div>
    <div class="field">City<span class="rule"></span></div>
    <div class="field">State<span class="rule"></span></div>
    <div class="field">Zip<span class="rule"></span></div>
    <div class="field">Email<span class="rule"></span></div>
    <div class="field">Sign up for our newsletter<span class="box"></span>Yes<span class="box"></span>No</div>
    <div class="field">Donation Amount<span class="rule"></span></div>
    <div class="field">Yes! I would like to make a monthly recurring donation</div>
    <div class="field">of ☐&nbsp; $25/month ☐&nbsp;&nbsp; $250/month ☐&nbsp;&nbsp; Other<span class="rule"></span></div>
    <div class="field">Please fill out the following if donating by credit card</div>
    <div class="field">(circle one)&nbsp;&nbsp;&nbsp;&nbsp; Vantage&nbsp;&nbsp;&nbsp; Meridian&nbsp;&nbsp;&nbsp; Ambit&nbsp;&nbsp;&nbsp; Dovetail</div>
    <div class="field">Credit Card#<span class="rule"></span></div>
    <div class="field">Exp Date<span class="rule"></span>CVC<span class="rule" style="flex:.35"></span></div>
    <div class="field">Signature<span class="rule"></span></div>
  </div>

  <p class="abs form-note">Please send your donation along with this form to<br><b>Blue Meadow Canine Allies</b><br>482 Orchard Lane, Suite 12<br>Fairview, IL 62000<br>All donations and contributions are tax deductible.</p>

  <div class="abs mini-brand"><span class="mark"></span><span>BLUE MEADOW<br>CANINE ALLIES</span></div>

  <div class="abs cover-brand"><span class="mark"></span>BLUE MEADOW CANINE ALLIES</div>

  <svg class="abs cover-shape" width="200" height="250" viewBox="0 0 200 250" aria-hidden="true">
    <path d="M0 250 V62 H60 C110 62 120 0 160 0 C185 0 200 8 200 8 V250 Z" fill="#3f6b36"/>
  </svg>
  <div class="abs cover-photo" role="img" aria-label="Black and white photo of a service dog resting on a soldier's shoulder"></div>
  <h1 class="abs cover-title">SUPPORT DOGS<br>FOR VETERANS AND<br>FIRST-RESPONDERS<br>WITH PTSD</h1>
  <div class="abs cover-url">www.bluemeadowcanineallies.com</div>
</section>

<!-- Inside sheet -->
<section class="sheet sheet--inside">
  <div class="abs panel-green"></div>

  <p class="abs body-text intro">Blue Meadow Canine Allies supports veterans and first-responders who have risked their lives to serve our country. To help those who struggle with Post Traumatic Stress Disorder (PTSD) as well as sexual trauma, Blue Meadow Canine Allies’ goal is to place trained PTSD service dogs with veterans and first-responders at no cost to help them heal from the psychological stress of war and duty through the compassion and healing power of their loyal 4-legged companions.</p>
  <div class="photo photo--light" style="left:148px;top:33px;width:112px;height:112px" role="img" aria-label="Group of trained service dogs sitting together at an event"></div>
  <div class="photo photo--dark" style="left:132px;top:137px;width:88px;height:88px" role="img" aria-label="Veteran kneeling to hug his service dog"></div>

  <h2 class="abs section-title mission-title">Our Mission</h2>
  <p class="abs body-text mission-text">Blue Meadow Canine Allies is committed to providing specialized service dogs to veterans suffering from post-traumatic stress disorder, traumatic brain injury, and/or sexual trauma. Our mission is to help these men and women regain their lives through the healing power of dogs.</p>

  <h2 class="abs section-title reality-title">The Reality</h2>
  <ul class="abs reality-list">
    <li>• 22 veterans and 1 active duty member commit suicide daily.</li>
    <li>• 15% of veterans suffer from PTSD or other major depressive disorders.</li>
    <li>• Only 30 to 40% of veterans who screen positive for serious emotional problems, PTSD, or depression seek mental healthcare.</li>
  </ul>

  <h2 class="abs hope-title">But there is hope!</h2>
  <ul class="abs hope-list">
    <li>Dogs are vigilant. They watch over their soldiers while they sleep, and wake them from nightmares.</li>
    <li>Dogs help relearn trust. They bring a sense of safety soldiers lose on the battlefield.</li>
    <li>Dogs create a bridge in public. They close the gap between a veteran and the world around them.</li>
    <li>Dogs help soldiers relearn how to give affection. War can be a place where love is forgotten and fear takes over.</li>
    <li>Dogs have a veteran’s back. They can be taught to sense and alert a veteran to an oncoming anxiety attack.</li>
    <li>In some instances, veterans with PTSD dogs are able to decrease their medication. Petting a dog elevates serotonin and dopamine—nerve transmitters that produce a calming state.</li>
  </ul>

  <div class="photo photo--dark" style="left:192px;top:293px;width:112px;height:112px" role="img" aria-label="Black service dog wearing a vest beside a small flag"></div>
  <div class="photo photo--light" style="left:314px;top:305px;width:104px;height:104px" role="img" aria-label="Veteran crouching beside his service dog in a hall"></div>
  <div class="photo photo--light" style="left:240px;top:369px;width:96px;height:96px" role="img" aria-label="Handler walking a service dog in training"></div>
  <div class="photo photo--dark" style="left:364px;top:376px;width:104px;height:104px" role="img" aria-label="Woman embracing her service dog"></div>

  <div class="abs banner" role="img" aria-label="Soldier in a helmet resting his head beside a dog"></div>
  <div class="abs banner-line1">They’ve had our backs</div>
  <div class="abs banner-line2">Now we’ve got theirs</div>

  <h2 class="abs section-title help-title">How can I help?</h2>
  <p class="abs help-text"><b>On average, it costs between $12,000 and $15,000 to train a PTSD service dog to certification due to the thousands of hours of specialty training involved.</b> Your generous donation allows Blue Meadow Canine Allies to offer highly trained support dogs at no cost to the veteran.</p>
  <p class="abs consider">To help, consider making a</p>
  <ul class="abs give-list">
    <li>• One-Time Gift</li>
    <li>• Monthly Giving</li>
    <li>• Planned Giving</li>
    <li>• Wills &amp; Bequests</li>
    <li>• Corporate Giving</li>
    <li>• Matching Gifts</li>
    <li>• Gifts of Stock</li>
    <li>• Wish List Donation</li>
  </ul>
  <div class="photo photo--light give-jar" role="img" aria-label="Hands holding a jar of coins labelled please help"></div>

  <p class="abs sponsor">Are you a company looking for a charity to sponsor? We would be happy to come to your workplace and give a presentation. Just contact us for more info.</p>
  <p class="abs contact">482 Orchard Lane, Suite 12 Fairview, IL 62000<br><span class="phone">555-014-2837</span><br>www.BlueMeadowCanineAllies.com</p>
</section>

</body>
</html>
```